Bright, Bold Sydney Tutoring Business Flyer Advertisment

Lumivora is an up and coming tutoring business located on Sydney's Upper North Shore catering to school students of all ages. We need a flyer designed for notice boards and letter box drops to attract new clients. Our tutors are mostly university education students who are fresh, dedicated and passionate about their areas of teaching. The flyer should exhibit a bright, bold, modern, clean cut style which would appeal to both students and parents. I have attached our logo (the flyer could reflect this colour scheme), and a PDF which outlines the information we would like to appear on the flyer. This is not set in stone, but designed to act as an extremely loose guide for your creativity !

Target Market(s)

Affluent School Students and Parents

Industry/Entity Type

Tutoring

Requirements
Must have
• Logo, $10 offer, company description.
Nice to have
• Grabbing headlines to attract new clients, such as "Feeling overwhelmed at school?". We are looking for an eye catching, clean cut and professional design that has the colours to attract kids and the tone to attract parents.

```html
<!DOCTYPE html>
<html lang="en">
<head>
<meta charset="utf-8">
<title>Lumivora Tutoring Flyer</title>
<link rel="stylesheet" href="https://fonts.googleapis.com/css2?family=Archivo+Black&family=Arimo:ital,wght@0,400;0,700;1,400&display=swap">
<style>
  :root {
    --teal: #84c9cb;
    --teal-deep: #7ac0c3;
    --teal-text: #7fc2c5;
    --pink-band: rgba(232, 150, 160, 0.55);
    --ink: #1e1a1a;
    --body: #2e2e2e;
    --white: #ffffff;
    --photo-light: #f4e6e6;
    --photo-mid: #e2b4b4;
    --photo-dark: #b98484;
  }
  * { margin: 0; padding: 0; box-sizing: border-box; }
  html, body { width: 1200px; height: 850px; overflow: hidden; background: var(--white); }
  .flyer {
    position: relative; width: 1200px; height: 850px; overflow: hidden;
    background: var(--white); font-family: "Arimo", Arial, sans-serif;
  }
  .hero-photo {
    position: absolute; left: 0; top: 0; width: 1200px; height: 425px;
    background:
      radial-gradient(ellipse 420px 260px at 330px 210px, var(--photo-mid), transparent 70%),
      radial-gradient(ellipse 500px 200px at 950px 330px, #ffffff, transparent 70%),
      linear-gradient(100deg, var(--photo-dark) 0%, var(--photo-mid) 30%, var(--photo-light) 60%, #f7f3f3 100%);
  }
  .contact-band {
    position: absolute; left: 0; top: 0; width: 1200px; height: 123px;
    background: var(--pink-band);
  }
  .contact-list {
    position: absolute; left: 52px; top: 34px; list-style: none;
    color: var(--white); font-weight: 700; font-size: 17px; line-height: 25px;
  }
  .brand-tile {
    position: absolute; left: 977px; top: 0; width: 117px; height: 140px;
    background: var(--white);
    display: flex; flex-direction: column; align-items: center; justify-content: center; gap: 10px;
  }
  .brand-dot { width: 40px; height: 40px; border-radius: 50%; background: var(--teal); }
  .brand-name { font-weight: 700; font-size: 20px; color: var(--ink); }
  .headlines {
    position: absolute; left: 0; top: 160px; width: 1200px; text-align: center;
    font-family: "Archivo Black", "Arial Black", sans-serif; color: var(--ink);
    text-shadow: 0 0 6px #fff, 0 0 10px #fff, 0 0 14px #fff;
  }
  .headline-main { font-size: 40px; line-height: 56px; letter-spacing: 0.5px; }
  .headline-sub { font-size: 26px; line-height: 53px; letter-spacing: 0.3px; }
  .offer-box {
    position: absolute; left: 165px; top: 345px; width: 870px; height: 156px;
    background: linear-gradient(100deg, var(--teal-deep), #a8dadb 50%, var(--teal-deep));
    border-radius: 3px;
    display: flex; align-items: center; justify-content: center; text-align: center;
    font-family: "Archivo Black", "Arial Black", sans-serif; color: var(--white);
    font-size: 38px; line-height: 46px; letter-spacing: 1px;
    text-shadow: 1px 2px 3px rgba(0,0,0,0.25);
  }
  .services-title {
    position: absolute; left: 90px; top: 520px;
    font-weight: 700; font-size: 29px; color: var(--teal-text);
  }
  .services-copy {
    position: absolute; left: 172px; top: 570px; width: 858px;
    font-size: 20px; line-height: 25px; color: var(--body); text-align: justify; text-align-last: justify;
  }
  .call-to-action {
    position: absolute; left: 0; top: 676px; width: 1170px; text-align: center;
    font-style: italic; font-size: 24px; line-height: 26px; color: var(--ink);
  }
  .footer-band {
    position: absolute; left: 165px; top: 755px; width: 870px; height: 95px;
    background: var(--teal);
  }
  .footer-brand {
    position: absolute; left: 65px; top: 0; width: 68px; height: 95px; background: var(--white);
    display: flex; flex-direction: column; align-items: center; justify-content: center; gap: 6px;
  }
  .footer-brand .brand-dot { width: 24px; height: 24px; }
  .footer-brand .brand-name { font-size: 11px; }
  .footer-url {
    position: absolute; left: 133px; top: 0; width: 737px; height: 95px;
    display: flex; align-items: center; justify-content: center;
    color: var(--white); font-weight: 700; font-size: 27px; letter-spacing: 0.5px;
  }
</style>
</head>
<body>
<main class="flyer">
  <div class="hero-photo" role="img" aria-label="Close-up photo of a student's hand writing with a pen in an open notebook"></div>
  <div class="contact-band"></div>
  <ul class="contact-list">
    <li>info@lumivoratutoring.com.au</li>
    <li>www.lumivoratutoring.com.au</li>
    <li>Suite 4, 218 Wattlegrove Road Kellsbrook, NSW 2079</li>
  </ul>
  <div class="brand-tile">
    <span class="brand-dot"></span>
    <span class="brand-name">lumivora</span>
  </div>

  <div class="headlines">
    <h1 class="headline-main">FEELING OVERWHELMED AT SCHOOL?</h1>
    <p class="headline-sub">LOOKING TO IMPROVE YOUR SKILLS, CONFIDENCE AND ORGANISATION?</p>
    <p class="headline-sub">WANT TO INCREASE YOUR CHILD’S ENGAGEMENT AT SCHOOL?</p>
  </div>

  <div class="offer-box">MENTION THIS ADVERTISEMENT<br>TO CLAIM YOUR TRIAL SESSION<br>FOR JUST $10!</div>

  <h2 class="services-title">OUR SERVICES :</h2>
  <p class="services-copy">Lumivora Tutoring offers one-on-one, individualised learning experiences to maximise academic development. Our tutors are hand selected on the basis of their qualifications, expertise and passion for inspiring young learners.</p>

  <p class="call-to-action">contact us today to discuss how we can help<br>make your learning goals a reality!</p>

  <footer class="footer-band">
    <div class="footer-brand">
      <span class="brand-dot"></span>
      <span class="brand-name">lumivora</span>
    </div>
    <div class="footer-url">WWW.LUMIVORATUTORING.COM.AU</div>
  </footer>
</main>
</body>
</html>
```